Dorian's Lawn Service needs a postcard design

I need a design to attract lawn cutting customers. I am a high school junior, focusing on my city and the neighboring city. I think it would be advantageous to let my potential clients know I am earning money for my college education. They should also know, I will be working side by side with my father, who operated his own lawn service for 20 years, so they can be assured of a quality result for their lawn. I will be using state of the art, commercial equipment.

A few things that are unique to my service are; my mower weighs half of what other commercial mowers do (a softer footprint), my mower does NOT throw clippings into mulch or flower beds, at an additional charge I offer bagging of the clippings and/or dog waste clean-up. I am thinking about a two-sided design. I would also like a cartoon style picture of myself riding my mower. If this is something you can create, I can send you a photo of myself and a photo of my mower. If not, I can get this drawing done separately, then send it to you, I would just need to know what kind of file you would need it in. I am not going to have a business name, I want to introduce myself as Dorian to keep it simple and personal. We can add a coupon to the postcard, offering one free cut with commitment to a full 26 week season. The name of my high school is Marlowe High.

The cartoon picture attached is our logo.

Target Market(s)

Homeowners that use a commercial lawn cutting service, homeowners that need a temporary service while they are on vacation

Industry/Entity Type

School

Colors
3176b5
9bcb3c

Requirements
Must have
• An appeal for people to want to help me earn money for my college education. A clear idea they will be getting top notch service. I definitely want a drawing of myself on my mower. Phone # 612-905-3817
• design must work with parcelvaro.com/routeflyermailing guidelines

```html
<!DOCTYPE html>
<html lang="en">
<head>
<meta charset="utf-8">
<title>Dorian's Lawn Service – Postcard</title>
<link rel="stylesheet" href="https://fonts.googleapis.com/css2?family=Yanone+Kaffeesatz:wght@400;500;700&family=Oswald:wght@500;600&family=Kaushan+Script&family=Indie+Flower&family=Arimo:wght@400;700&display=swap">
<style>
  :root {
    --page: #ffffff;
    --sky-top: #3d86d8;
    --sky-low: #a9d3f0;
    --lawn-light: #7fc13f;
    --lawn-dark: #2f7d1e;
    --lawn-deep: #24661a;
    --lime: #e4f56b;
    --lime-line: #c8ec4a;
    --white: #ffffff;
    --ink: #1b1b1b;
    --badge-sky: #bfe3f2;
    --badge-grass: #5aa83a;
    --shadow: rgba(0,0,0,0.35);
  }
  * { box-sizing: border-box; margin: 0; padding: 0; }
  html, body { width: 920px; height: 1200px; overflow: hidden; background: var(--page); }
  .canvas { position: relative; width: 920px; height: 1200px; }

  .card {
    position: absolute; left: 30px; width: 860px; height: 556px;
    overflow: hidden; box-shadow: 0 3px 10px var(--shadow);
  }
  .card--front { top: 30px; }
  .card--back { top: 620px; background: var(--white); }

  .scene-photo {
    position: absolute; inset: 0;
    background: linear-gradient(180deg, var(--sky-top) 0%, var(--sky-low) 42%, var(--lawn-light) 50%, var(--lawn-dark) 100%);
  }
  .mascot {
    position: absolute; border-radius: 50%;
    background: radial-gradient(circle at 50% 40%, var(--badge-sky) 0%, var(--badge-sky) 55%, var(--badge-grass) 100%);
  }
  .mascot--large { left: 498px; top: 156px; width: 296px; height: 296px; }
  .mascot--small { left: 31px; top: 30px; width: 154px; height: 154px; }

  .headline {
    position: absolute; right: 46px; font-family: "Yanone Kaffeesatz", sans-serif;
    font-size: 44px; color: var(--lime); line-height: 1; text-align: right;
    text-shadow: 0 2px 3px rgba(0,0,0,0.35);
  }
  .headline--one { top: 54px; }
  .headline--two { top: 113px; }
  .headline .caps {
    font-family: "Oswald", sans-serif; font-weight: 600; font-size: 32px;
    color: var(--white); letter-spacing: 1px;
  }

  .pitch { position: absolute; left: 20px; width: 420px; text-align: center; color: var(--white); text-shadow: 0 2px 3px rgba(0,0,0,0.45); }
  .pitch__hire { top: 258px; font-family: "Oswald", sans-serif; font-weight: 600; font-size: 36px; letter-spacing: 2px; line-height: 1.2; }
  .pitch__price { top: 308px; font-family: "Yanone Kaffeesatz", sans-serif; font-size: 33px; color: var(--lime); }
  .pitch__help { top: 356px; font-family: "Indie Flower", cursive; font-size: 19px; letter-spacing: 1px; line-height: 1.8; text-transform: uppercase; }

  .phone-line {
    position: absolute; font-family: "Oswald", sans-serif; font-weight: 600;
    color: var(--white); letter-spacing: 3px; white-space: nowrap;
    text-shadow: 0 2px 4px rgba(0,0,0,0.5);
  }
  .phone-line span + span { margin-left: 34px; }
  .card--front .phone-line { left: 198px; top: 466px; font-size: 41px; }

  .back-photo {
    position: absolute; left: 0; top: 0; width: 709px; height: 556px;
    background: linear-gradient(160deg, var(--lawn-light) 0%, var(--lawn-dark) 55%, var(--lawn-deep) 100%);
  }
  .tagline {
    position: absolute; left: 188px; top: 36px; font-family: "Kaushan Script", cursive;
    font-size: 28px; color: var(--lime); white-space: nowrap;
    text-shadow: 0 2px 3px rgba(0,0,0,0.35);
  }
  .story {
    position: absolute; font-family: "Yanone Kaffeesatz", sans-serif; font-weight: 500;
    font-size: 19px; line-height: 22px; color: var(--white);
    text-shadow: 0 1px 3px rgba(0,0,0,0.6);
  }
  .story--intro { left: 190px; top: 90px; width: 520px; }
  .story--equipment { left: 34px; top: 186px; width: 470px; }

  .coupon {
    position: absolute; left: 32px; top: 286px; width: 182px; height: 104px;
    border: 3px dashed var(--lime-line); border-radius: 10px;
    text-align: center; color: var(--white); padding-top: 12px;
  }
  .coupon__title { font-family: "Oswald", sans-serif; font-weight: 500; font-size: 21px; letter-spacing: 1px; }
  .coupon__terms { font-family: "Yanone Kaffeesatz", sans-serif; font-weight: 500; font-size: 15px; line-height: 17px; margin-top: 6px; }

  .extras {
    position: absolute; left: 30px; top: 406px; width: 190px; height: 114px;
    border: 3px solid var(--lime-line); border-radius: 14px; color: var(--white); padding: 6px 8px;
  }
  .extras__title { font-family: "Oswald", sans-serif; font-weight: 500; font-size: 14px; text-align: center; letter-spacing: 0.5px; }
  .extras__text { font-family: "Yanone Kaffeesatz", sans-serif; font-weight: 500; font-size: 15px; line-height: 17px; margin-top: 6px; letter-spacing: 0.4px; }

  .card--back .phone-line { left: 266px; top: 482px; font-size: 38px; }
  .card--back .phone-line span + span { margin-left: 14px; }

  .indicia, .address {
    position: absolute; border: 2px solid var(--ink); font-family: "Arimo", sans-serif; color: var(--ink);
    writing-mode: vertical-rl; transform: rotate(180deg);
  }
  .indicia {
    left: 731px; top: 25px; width: 112px; height: 112px; border-width: 1.5px;
    font-size: 12.5px; line-height: 15px; text-align: center; padding: 6px 8px;
    display: flex; flex-direction: column; justify-content: center; align-items: center;
  }
  .indicia .paid { font-weight: 700; }
  .address {
    left: 724px; top: 172px; width: 122px; height: 340px; padding: 18px 14px;
    display: flex; flex-direction: column; justify-content: flex-start;
  }
  .address__route { font-size: 14px; letter-spacing: 0.5px; margin-bottom: 18px; }
  .address__name { font-size: 21px; line-height: 26px; }
</style>
</head>
<body>
<main class="canvas">

  <section class="card card--front" aria-label="Postcard front">
    <div class="scene-photo" role="img" aria-label="Photo of a freshly striped green lawn with trees and a white house under a blue summer sky"></div>
    <p class="headline headline--one">Looking for a top notch <span class="caps">LAWN</span></p>
    <p class="headline headline--two"><span class="caps">CUTTING</span> service this summer?</p>
    <div class="mascot mascot--large" role="img" aria-label="Cartoon of Dorian in a red cap and Marlowe High shirt riding a green zero-turn mower"></div>
    <h1 class="pitch pitch__hire">HIRE DORIAN</h1>
    <p class="pitch pitch__price">for a beautiful lawn at a great price</p>
    <p class="pitch pitch__help">And help a local high school student<br>earn money for college!</p>
    <p class="phone-line"><span>DORIAN</span><span>612-905-3817</span></p>
  </section>

  <section class="card card--back" aria-label="Postcard back">
    <div class="back-photo" role="img" aria-label="Photo of a happy white and brown dog rolling on its back in thick green grass"></div>
    <div class="mascot mascot--small" role="img" aria-label="Cartoon of Dorian riding his mower"></div>
    <p class="tagline">Relax and enjoy a beautiful lawn this summer . . .</p>
    <p class="story story--intro">I really am a local high school student working to earn money for college. You can be assured of high-quality results with my service. I will be working side by side with my father, who operated his own lawn service for 20 years.</p>
    <p class="story story--equipment">I will be using state of the art, commercial equipment. My mower weighs half of what other commercial mowers do (a softer footprint), and does NOT throw clippings into mulch or flower beds.</p>

    <div class="coupon">
      <p class="coupon__title">FREE LAWN CUT</p>
      <p class="coupon__terms">with commitment to a full<br>26 week summer season</p>
    </div>

    <div class="extras">
      <p class="extras__title">ADDITIONAL SERVICES</p>
      <p class="extras__text">I offer bagging of the clippings and/or dog waste clean-up for a small extra charge.</p>
    </div>

    <p class="phone-line"><span>DORIAN</span><span>612-905-3817</span></p>

    <div class="indicia">
      <span>PRSRT STD</span>
      <span>ECRWSS</span>
      <span>U.S. POSTAGE</span>
      <span class="paid">PAID</span>
      <span>RFM RETAIL</span>
    </div>

    <div class="address">
      <span class="address__route">****************ECRWSS****</span>
      <span class="address__name">Local<br>Postal Customer</span>
    </div>
  </section>

</main>
</body>
</html>
```